business card design

i would like business cards designed. My business provides trade qualified personnel to the mining industry to work on heavy mobile equipment.
please put a excavator(digger) in the background in one design and have one design without so i can compare the difference.
also add info:
my logo(attached) and "mobile equipment repair and maintenance"
name: Derek Holloway
address: 57 Tarrowby RD Kestwick Hills WA.
mobile: 0438120957
email: derek@ironvalemx.com

```html
<!DOCTYPE html>
<html lang="en">
<head>
<meta charset="utf-8">
<title>Ironvale Maintenance Services – Business Cards</title>
<link href="https://fonts.googleapis.com/css2?family=Montserrat:ital,wght@0,400;0,500;0,700;0,800;1,800&display=swap" rel="stylesheet">
<style>
  :root {
    --page-bg: #1c1d20;
    --card-navy: #0a1f3e;
    --accent-blue: #4674c4;
    --text-white: #f2f5fa;
    --faint-mark: #163562;
  }
  * { margin: 0; padding: 0; box-sizing: border-box; }
  html, body {
    width: 1200px; height: 900px; overflow: hidden;
    background: var(--page-bg);
    font-family: "Montserrat", sans-serif;
  }
  .sheet {
    width: 1200px; height: 900px;
    display: flex; flex-direction: column;
    align-items: center; justify-content: center; gap: 40px;
  }
  .card {
    position: relative;
    width: 660px; height: 403px;
    background: var(--card-navy);
    border-bottom: 12px solid var(--accent-blue);
    box-shadow: 0 14px 30px rgba(0,0,0,0.55);
    overflow: hidden;
  }
  /* Front */
  .holder-name {
    position: absolute; left: 44px; top: 58px;
    color: var(--accent-blue);
    font-weight: 800; font-style: italic;
    font-size: 21px; letter-spacing: 1.2px; text-transform: uppercase;
  }
  .divider {
    position: absolute; left: 44px; right: 44px; top: 160px;
    height: 1.5px; background: var(--accent-blue);
  }
  .contact-list {
    position: absolute; left: 44px; top: 188px;
    list-style: none; color: var(--text-white);
    font-size: 17px; font-weight: 400; letter-spacing: 0.6px;
  }
  .contact-list li { display: flex; align-items: center; gap: 12px; margin-bottom: 12px; }
  .contact-list svg { width: 16px; height: 16px; fill: var(--text-white); }
  .brand {
    position: absolute; right: 44px; top: 78px; text-align: left;
  }
  .brand-name {
    color: var(--text-white);
    font-weight: 800; font-size: 40px; letter-spacing: 3px; line-height: 1;
  }
  .brand-sub {
    margin-top: 8px;
    color: var(--accent-blue);
    font-weight: 500; font-size: 10.5px; letter-spacing: 1.4px;
  }
  .address {
    position: absolute; right: 44px; bottom: 48px; text-align: right;
    color: var(--text-white); font-style: normal;
    font-size: 19px; font-weight: 400; letter-spacing: 0.8px; line-height: 1.45;
  }
  /* Back */
  .back-mark {
    position: absolute; left: 0; right: 0; top: 110px; text-align: center;
  }
  .back-mark .brand-name {
    color: var(--faint-mark); font-size: 86px; letter-spacing: 8px;
  }
  .back-mark .brand-sub {
    color: var(--faint-mark); font-size: 18px; letter-spacing: 3px; margin-top: 10px;
  }
  .tagline {
    position: absolute; left: 0; right: 0; bottom: 60px; text-align: center;
    color: var(--text-white);
    font-size: 17px; font-weight: 400; letter-spacing: 1.8px; text-transform: uppercase;
  }
</style>
</head>
<body>
<main class="sheet">
  <section class="card card-front">
    <h1 class="holder-name">Derek Holloway</h1>
    <div class="brand">
      <div class="brand-name">IRONVALE</div>
      <div class="brand-sub">MAINTENANCE SERVICES PTY LTD</div>
    </div>
    <div class="divider"></div>
    <ul class="contact-list">
      <li>
        <svg viewBox="0 0 24 24" aria-hidden="true"><path d="M6.6 10.8a15.1 15.1 0 0 0 6.6 6.6l2.2-2.2a1 1 0 0 1 1-.25 11.4 11.4 0 0 0 3.6.57 1 1 0 0 1 1 1V20a1 1 0 0 1-1 1A17 17 0 0 1 3 4a1 1 0 0 1 1-1h3.5a1 1 0 0 1 1 1c0 1.25.2 2.45.57 3.6a1 1 0 0 1-.25 1z"/></svg>
        <span>0438120957</span>
      </li>
      <li>
        <svg viewBox="0 0 24 24" aria-hidden="true"><path d="M2 5h20v14H2zm2 2v.4l8 5 8-5V7zm0 2.8V17h16V9.8l-8 5z"/></svg>
        <span>derek@ironvalemx.com</span>
      </li>
    </ul>
    <address class="address">57 Tarrowby RD<br>Kestwick Hills WA.</address>
  </section>

  <section class="card card-back">
    <div class="back-mark">
      <div class="brand-name">IRONVALE</div>
      <div class="brand-sub">MAINTENANCE SERVICES PTY LTD</div>
    </div>
    <p class="tagline">Mobile Equipment Repair and Maintenance</p>
  </section>
</main>
</body>
</html>
```